Direct Mail Postcard- Lighting Company

Our task is to send a postcard directly to houses surrounding where our company has done work. My goal is to position ourselves as the go to outdoor lighting partner for their neighborhood.
Trusted Lighting Design & Maintenance Your neighbor chose us to enhance and maintain their home's beauty and security. Now, we're offering our top-tier services to the entire neighborhood.
Please emphasize our:
Maintenance Excellence:
Regular system check-ups
Prompt repair and replacement
Upgrades to the latest technology
Less emphasis on:
Our Services:
High-Quality Landscape & Architectural Lighting
Reliable Permanent Lighting Solutions
Call us today and take advantage of our 25% discount (limited time offer)
For more details or to schedule a consultation, visit brightvane-mo.com or call .
*Need to be able to tweak this for future campaigns. Quickly edit verbiage for future marketing campaigns. I.e. a file that can be edited through Canva
*Inspiration photo file (Yard Glow Horizons)
*Would like to incorporate the before and after png
Call: (816) 555-0193
brightvane-mo.com
Updates
I attached a new before and after photo. Please create a design implementing this
Look and feel
Each slider illustrates characteristics of the customer's brand and the style your logo design should communicate.

```html
<!DOCTYPE html>
<html lang="en">
<head>
<meta charset="utf-8">
<title>Brightvane Lighting – Direct Mail Postcard</title>
<link href="https://fonts.googleapis.com/css2?family=Oswald:wght@400;600;700&family=Montserrat:wght@300;400;600&display=swap" rel="stylesheet">
<style>
  :root{
    --stage:#1f3a2a;
    --card:#1b1d25;
    --card-deep:#121319;
    --yellow:#f5d823;
    --amber:#f0a43a;
    --orange:#f07a1f;
    --green:#3fae49;
    --white:#ffffff;
    --muted:#c9ccd3;
    --dusk-top:#2c3f66;
    --dusk-mid:#4a5270;
    --glow:#d98a3c;
    --night:#0f1420;
  }
  *{box-sizing:border-box;margin:0;padding:0}
  html,body{width:1200px;height:2908px;overflow:hidden}
  body{background:var(--stage);font-family:'Montserrat',sans-serif;color:var(--white)}
  .postcard{position:absolute;left:170px;width:860px;height:1290px;overflow:hidden;
    background:linear-gradient(180deg,var(--card) 0%,var(--card-deep) 100%);box-shadow:0 20px 50px rgba(0,0,0,.45)}
  .postcard--front{top:114px}
  .postcard--back{top:1504px}

  /* front */
  .front-headline{position:absolute;left:0;right:0;top:40px;text-align:center;font-family:'Oswald',sans-serif;text-transform:uppercase;line-height:1.1}
  .front-headline .line-a{font-size:46px;font-weight:700}
  .front-headline .line-b{font-size:38px;font-weight:400}
  .front-headline .line-c{font-size:48px;font-weight:700;color:var(--yellow)}
  .hero-photo{position:absolute;left:0;top:250px;width:860px;height:600px;
    background:linear-gradient(180deg,var(--dusk-top) 0%,var(--dusk-mid) 45%,var(--glow) 78%,var(--night) 100%)}
  .hero-oval{position:absolute;left:180px;top:410px;width:300px;height:470px;border:8px solid var(--white);border-radius:50%;
    background:radial-gradient(circle at 50% 45%,rgba(255,220,120,.55),rgba(0,0,0,.1) 60%)}
  .hero-oval svg{position:absolute;left:90px;top:140px}
  .discount{position:absolute;width:180px;height:180px;border-radius:50%;border:8px solid var(--green);background:var(--card-deep);
    display:flex;flex-direction:column;align-items:center;justify-content:center;font-family:'Oswald',sans-serif}
  .discount .label{font-size:17px;letter-spacing:2px;color:var(--white)}
  .discount .value{font-size:62px;font-weight:700;color:var(--yellow);line-height:1}
  .postcard--front .discount{left:650px;top:290px}
  .service-cols{position:absolute;left:50px;right:50px;top:880px;display:flex;justify-content:space-between;gap:40px}
  .service-cols h3{font-family:'Oswald',sans-serif;font-size:22px;color:var(--amber);text-transform:uppercase;margin-bottom:8px}
  .service-cols li{list-style:none;font-size:16px;line-height:1.45;color:var(--muted)}
  .brand{position:absolute;left:0;right:0;text-align:center;font-family:'Montserrat',sans-serif;font-weight:300;letter-spacing:10px;text-transform:uppercase;color:var(--white)}
  .brand .name{display:block;font-size:52px}
  .brand .sub{display:block;font-size:20px;letter-spacing:14px;margin-top:4px}
  .postcard--front .brand{top:1050px}
  .call{position:absolute;left:0;right:0;text-align:center;font-family:'Oswald',sans-serif;font-weight:700;font-size:52px;color:var(--yellow)}
  .postcard--front .call{top:1160px}
  .site{position:absolute;left:0;right:0;text-align:center;font-size:18px;color:var(--muted)}
  .postcard--front .site{top:1242px}

  /* back */
  .back-headline{position:absolute;right:40px;top:40px;width:400px;text-align:center;font-family:'Oswald',sans-serif;text-transform:uppercase;line-height:1.05}
  .back-headline .line-a{font-size:62px;font-weight:700;color:var(--yellow)}
  .back-headline .line-b{font-size:48px;font-weight:600}
  .back-headline .band{display:inline-block;margin-top:8px;padding:4px 18px;background:var(--yellow);color:var(--card-deep);font-size:36px;font-weight:700}
  .photo-circle{position:absolute;border-radius:50%;border:10px solid var(--amber)}
  .photo-before{left:-140px;top:-60px;width:640px;height:640px;background:radial-gradient(circle at 60% 60%,#3a4150,var(--night) 75%)}
  .photo-after{left:380px;top:400px;width:460px;height:460px;background:linear-gradient(180deg,var(--dusk-top) 0%,var(--dusk-mid) 50%,var(--glow) 85%,var(--night) 100%)}
  .bulb-ring{position:absolute;left:300px;top:440px;width:150px;height:150px;border-radius:50%;border:6px solid var(--yellow);background:var(--card-deep);display:flex;align-items:center;justify-content:center}
  .tag{position:absolute;font-family:'Oswald',sans-serif;font-weight:700;font-size:44px;color:var(--orange);letter-spacing:4px}
  .tag-before{left:150px;top:620px;transform:rotate(-40deg)}
  .tag-after{left:410px;top:330px;transform:rotate(-40deg)}
  .postcard--back .discount{left:80px;top:780px}
  .review-badge{position:absolute;left:610px;top:900px;width:160px;height:84px;border-radius:6px;background:var(--white)}
  .postcard--back .brand{top:1020px}
  .postcard--back .site{top:1130px}
  .postcard--back .call{top:1170px}
</style>
</head>
<body>

<section class="postcard postcard--front">
  <div class="front-headline">
    <div class="line-a">Elevate Your Outdoor Spaces</div>
    <div class="line-b">With Premium Lighting Trusted</div>
    <div class="line-c">Lighting Design &amp; Maintenance</div>
  </div>
  <div class="hero-photo" role="img" aria-label="Photo of a two-storey home at dusk with warm landscape and architectural lighting"></div>
  <div class="hero-oval">
    <svg width="120" height="170" viewBox="0 0 120 170" aria-hidden="true">
      <path d="M60 8a46 46 0 0 0-28 82c8 7 12 16 12 26h32c0-10 4-19 12-26A46 46 0 0 0 60 8z" fill="#f5d823"/>
      <rect x="44" y="122" width="32" height="10" rx="3" fill="#c9ccd3"/>
      <rect x="46" y="136" width="28" height="10" rx="3" fill="#c9ccd3"/>
      <rect x="52" y="150" width="16" height="8" rx="3" fill="#c9ccd3"/>
    </svg>
  </div>
  <div class="discount"><span class="label">DISCOUNT</span><span class="value">25%</span></div>
  <div class="service-cols">
    <div>
      <h3>Maintenance Excellence</h3>
      <ul><li>Regular system check-ups</li><li>Prompt repair and replacement</li><li>Upgrades to the latest technology</li></ul>
    </div>
    <div>
      <h3>Our Services</h3>
      <ul><li>High-Quality Landscape &amp; Architectural Lighting</li><li>Reliable Permanent Lighting Solutions</li></ul>
    </div>
  </div>
  <div class="brand"><span class="name">Brightvane</span><span class="sub">Lighting</span></div>
  <div class="call">Call (816) 555-0193</div>
  <div class="site">www.brightvane-mo.com</div>
</section>

<section class="postcard postcard--back">
  <div class="photo-circle photo-before" role="img" aria-label="Before photo: the home at night without outdoor lighting"></div>
  <div class="photo-circle photo-after" role="img" aria-label="After photo: the same home at night with warm outdoor lighting"></div>
  <div class="bulb-ring">
    <svg width="70" height="100" viewBox="0 0 120 170" aria-hidden="true">
      <path d="M60 8a46 46 0 0 0-28 82c8 7 12 16 12 26h32c0-10 4-19 12-26A46 46 0 0 0 60 8z" fill="#f5d823"/>
      <rect x="44" y="122" width="32" height="10" rx="3" fill="#c9ccd3"/>
      <rect x="46" y="136" width="28" height="10" rx="3" fill="#c9ccd3"/>
    </svg>
  </div>
  <div class="tag tag-before">BEFORE</div>
  <div class="tag tag-after">AFTER</div>
  <div class="back-headline">
    <div class="line-a">Create Magic</div>
    <div class="line-b">At Night With</div>
    <div class="band">The Perfect Glow</div>
  </div>
  <div class="discount"><span class="label">DISCOUNT</span><span class="value">25%</span></div>
  <div class="review-badge" aria-hidden="true"></div>
  <div class="brand"><span class="name">Brightvane</span><span class="sub">Lighting</span></div>
  <div class="site">www.brightvane-mo.com</div>
  <div class="call">Call (816) 555-0193</div>
</section>

</body>
</html>
```